Quorivel Flyer for Logistics Fair

We are a leading Shelving & Warehouse Systems Specialist supplying consultancy, design and end to end project implementation for Retail and Warehouses. We seek a brochure that is simple yet communicates our products and services in a handout pamphlet.

Target Market(s)

Warehouse and Factory buyers looking for racks needed in their facility

Industry/Entity Type

Retail

Font styles to use
Serif
Sans Serif

Colors
000000

Requirements
Must have
• Company name and logo ( Quorivel)
• Pictures of Rack & Conveying systems
• Products we do
• Services we provide
• Focus on " Soecialist in Retail & Warehouses Solutions "
Nice to have
• Easy to understand layout and flow
• Modern-day and trendy feel
Should not have
• Not be cluttered
• Not too wordy
• Pls do not use pic of factory or equipments .....

```html
<!DOCTYPE html>
<html lang="en">
<head>
<meta charset="utf-8">
<title>Quorivel – Flyer for Logistics Fair</title>
<link rel="stylesheet" href="https://fonts.googleapis.com/css2?family=Montserrat:wght@800&family=Oswald:wght@400;500&family=Roboto:wght@400;700&display=swap">
<style>
  :root{
    --page:#e4e4e4;
    --paper:#efefef;
    --charcoal:#333333;
    --ink:#1b1b1b;
    --brand-blue:#1e6fb4;
    --accent-blue:#1a9ad6;
    --white:#ffffff;
    --footer-bar:rgba(235,235,235,.92);
  }
  *{margin:0;padding:0;box-sizing:border-box}
  html,body{width:1200px;height:1040px;overflow:hidden;background:var(--page)}
  .canvas{position:relative;width:1200px;height:1040px}
  .flyer{position:absolute;left:203px;top:20px;width:811px;height:1021px;transform:scale(.979);transform-origin:0 0;overflow:hidden;background:var(--paper);box-shadow:0 6px 18px rgba(0,0,0,.25)}
  .backdrop{position:absolute;inset:0}
  .hero-title{position:absolute;left:48px;top:56px;color:var(--white)}
  .hero-title .brand{font-family:"Montserrat",sans-serif;font-weight:800;font-size:72px;letter-spacing:1px;line-height:1}
  .hero-title .event{font-family:"Oswald",sans-serif;font-weight:500;font-size:58px;line-height:1.1;margin-top:4px}

  .racks{position:absolute;left:21px;top:398px;width:424px}
  .racks h2{font-family:"Oswald",sans-serif;font-weight:400;font-size:28px;color:var(--brand-blue);white-space:nowrap}
  .rack-grid{display:flex;justify-content:space-between;margin-top:14px}
  .rack{width:134px}
  .rack-photo{width:134px;height:76px;border:1px solid var(--brand-blue)}
  .rack-photo.server{background:linear-gradient(120deg,#2c4d6e,#9fb8cc 55%,#e9eef2)}
  .rack-photo.aisle{background:linear-gradient(90deg,#b25a1c,#e6a35c 45%,#5c4a3a 55%,#d2782c)}
  .rack-photo.stock{background:linear-gradient(120deg,#d9751c,#f0c24a 50%,#c6602a)}
  .rack h3{font-family:"Roboto",sans-serif;font-weight:700;font-size:20px;text-align:center;margin:12px 0 14px;color:var(--ink)}
  .rack p{font-family:"Roboto",sans-serif;font-size:11.4px;line-height:15.6px;text-align:justify;color:var(--ink);hyphens:auto}

  .services{position:absolute;left:527px;top:325px;width:270px;color:var(--white)}
  .services h2{font-family:"Oswald",sans-serif;font-weight:400;font-size:30px;margin-left:10px;margin-bottom:10px}
  .service{margin-bottom:14px}
  .service-head{display:flex;align-items:center;gap:12px;margin-left:3px}
  .service-icon{width:60px;height:54px;background:var(--white);border-radius:6px;display:flex;align-items:center;justify-content:center;flex:none}
  .service-head h3{font-family:"Oswald",sans-serif;font-weight:400;font-size:20px;line-height:28px}
  .service p{font-family:"Roboto",sans-serif;font-size:12px;line-height:16px;margin-top:14px}

  .products{position:absolute;left:30px;top:762px;width:540px;color:var(--white)}
  .products h2{font-family:"Oswald",sans-serif;font-weight:500;font-size:38px;text-align:center;margin-left:84px}
  .product-row{display:flex;justify-content:space-between;align-items:flex-end;margin-top:14px;padding-right:6px}
  .product{text-align:center;font-family:"Oswald",sans-serif;font-size:22px;white-space:nowrap}
  .product svg{display:block;margin:0 auto 8px}

  .footer-brand{position:absolute;left:32px;top:956px;font-family:"Montserrat",sans-serif;font-weight:800;font-size:44px;color:var(--white);letter-spacing:1px}
  .contact-bar{position:absolute;left:352px;top:962px;width:459px;height:33px;background:var(--footer-bar);display:flex;align-items:center;justify-content:space-around;font-family:"Oswald",sans-serif;font-size:14px;color:var(--ink)}
  .contact-bar span{display:flex;align-items:center;gap:6px}
</style>
</head>
<body>
<div class="canvas">
  <article class="flyer">
    <svg class="backdrop" width="811" height="1021" viewBox="0 0 811 1021">
      <defs>
        <linearGradient id="airport" x1="0" y1="0" x2="0" y2="1">
          <stop offset="0" stop-color="#5f8fab"/>
          <stop offset=".5" stop-color="#2f5a78"/>
          <stop offset="1" stop-color="#17364d"/>
        </linearGradient>
        <linearGradient id="skyline" x1="0" y1="0" x2="0" y2="1">
          <stop offset="0" stop-color="#7a7a7a"/>
          <stop offset="1" stop-color="#3a3a3a"/>
        </linearGradient>
      </defs>
      <path role="img" aria-label="Airport apron with a cargo jet being loaded, tinted blue" d="M0 0H811V360L520 368C330 368 150 292 0 211Z" fill="url(#airport)"/>
      <path d="M0 214C150 296 330 372 520 372" fill="none" stroke="var(--accent-blue)" stroke-width="9"/>
      <path role="img" aria-label="Grey city skyline of high-rise buildings" d="M0 842C150 768 340 732 500 732H811V1021H0Z" fill="url(#skyline)"/>
      <path d="M0 838C150 764 340 728 500 728H560" fill="none" stroke="var(--accent-blue)" stroke-width="10"/>
      <circle cx="887" cy="561" r="434" fill="none" stroke="#c9cdd1" stroke-width="3" opacity=".8"/>
      <circle cx="887" cy="561" r="420" fill="var(--charcoal)"/>
    </svg>

    <header class="hero-title">
      <div class="brand">QUORIVEL</div>
      <div class="event">FOR LOGISTICS FAIR</div>
    </header>

    <section class="racks">
      <h2>Pictures of Rack &amp; Conveying systems</h2>
      <div class="rack-grid">
        <div class="rack">
          <div class="rack-photo server" role="img" aria-label="Technician with laptop beside server racks"></div>
          <h3>Rack1</h3>
          <p>Lorem ipsum dolor sit amet, consectetuer adipiscing elit. Aenean commodo ligula eget dolor. Aenean massa. Cum sociis natoque penatibus et magnis dis parturient montes, nascetur ridiculus mus.</p>
        </div>
        <div class="rack">
          <div class="rack-photo aisle" role="img" aria-label="Warehouse aisle lined with orange pallet racks"></div>
          <h3>Rack2</h3>
          <p>Lorem ipsum dolor sit amet, consectetuer adipiscing elit. Aenean commodo ligula eget dolor. Aenean massa. Cum sociis natoque penatibus et magnis dis parturient montes, nascetur ridiculus mus.</p>
        </div>
        <div class="rack">
          <div class="rack-photo stock" role="img" aria-label="Worker standing in front of stocked shelving"></div>
          <h3>Rack3</h3>
          <p>Lorem ipsum dolor sit amet, consectetuer adipiscing elit. Aenean commodo ligula eget dolor. Aenean massa. Cum sociis natoque penatibus et magnis dis parturient montes, nascetur ridiculus mus.</p>
        </div>
      </div>
    </section>

    <section class="services">
      <h2>Services We Provide</h2>
      <div class="service">
        <div class="service-head">
          <div class="service-icon">
            <svg width="44" height="44" viewBox="0 0 44 44"><circle cx="22" cy="22" r="18" fill="none" stroke="#1a8fd0" stroke-width="4"/><path d="M22 11V23H30" fill="none" stroke="#1a8fd0" stroke-width="3.5" stroke-linecap="round"/></svg>
          </div>
          <h3>Infrastructure<br>Services</h3>
        </div>
        <p>Aenean imperdiet. Etiam ultricies nisi vel augue. Curabitur ullamcorper ultricies nisi. Nam eget dui Etiam rhoncus.</p>
      </div>
      <div class="service">
        <div class="service-head">
          <div class="service-icon">
            <svg width="44" height="44" viewBox="0 0 44 44"><g fill="#1a8fd0"><circle cx="22" cy="22" r="14"/><rect x="18" y="2" width="8" height="40" rx="1"/><rect x="18" y="2" width="8" height="40" rx="1" transform="rotate(45 22 22)"/><rect x="18" y="2" width="8" height="40" rx="1" transform="rotate(90 22 22)"/><rect x="18" y="2" width="8" height="40" rx="1" transform="rotate(135 22 22)"/></g><circle cx="22" cy="22" r="6" fill="#fff"/></svg>
          </div>
          <h3>Management<br>Services</h3>
        </div>
        <p>Aenean imperdiet. Etiam ultricies nisi vel augue. Curabitur ullamcorper ultricies nisi. Nam eget dui Etiam rhoncus.</p>
      </div>
      <div class="service">
        <div class="service-head">
          <div class="service-icon">
            <svg width="46" height="40" viewBox="0 0 46 40"><rect x="2" y="2" width="42" height="28" rx="2" fill="none" stroke="#1a8fd0" stroke-width="3"/><path d="M18 30L15 37H31L28 30" fill="none" stroke="#1a8fd0" stroke-width="3"/></svg>
          </div>
          <h3>Analytical<br>Services</h3>
        </div>
        <p>Aenean imperdiet. Etiam ultricies nisi vel augue. Curabitur ullamcorper ultricies nisi. Nam eget dui Etiam rhoncus.</p>
      </div>
    </section>

    <section class="products">
      <h2>Products We Do</h2>
      <div class="product-row">
        <div class="product">
          <svg width="92" height="64" viewBox="0 0 92 64"><path d="M2 4H14L24 44H80L88 16H20" fill="none" stroke="#fff" stroke-width="4" stroke-linejoin="round"/><circle cx="32" cy="56" r="5" fill="none" stroke="#fff" stroke-width="4"/><circle cx="72" cy="56" r="5" fill="none" stroke="#fff" stroke-width="4"/></svg>
          Packaged of Goods
        </div>
        <div class="product">
          <svg width="104" height="58" viewBox="0 0 104 58"><rect x="36" y="2" width="66" height="40" fill="#fff"/><path d="M34 14H18L4 30V46H34Z" fill="#fff"/><path d="M14 28L20 20H28V28Z" fill="#555"/><circle cx="20" cy="48" r="8" fill="#fff" stroke="#555" stroke-width="3"/><circle cx="82" cy="48" r="8" fill="#fff" stroke="#555" stroke-width="3"/></svg>
          Transport
        </div>
        <div class="product">
          <svg width="92" height="76" viewBox="0 0 92 76"><rect x="6" y="10" width="24" height="26" fill="none" stroke="#fff" stroke-width="3.5"/><path d="M12 10V2M24 10V2" stroke="#fff" stroke-width="3.5"/><path d="M18 36V56C18 70 44 70 44 56V40C44 30 60 30 60 42V50" fill="none" stroke="#fff" stroke-width="3.5"/><rect x="56" y="50" width="30" height="22" fill="none" stroke="#fff" stroke-width="3.5"/></svg>
          Warehousing
        </div>
        <div class="product">
          <svg width="80" height="80" viewBox="0 0 80 80"><path d="M40 4L76 20V60L40 76L4 60V20Z" fill="#fff"/><path d="M4 20L40 36L76 20M40 36V76" fill="none" stroke="#555" stroke-width="3"/><path d="M22 12L58 28V38" fill="none" stroke="#555" stroke-width="5"/></svg>
          Delivery
        </div>
      </div>
    </section>

    <div class="footer-brand">QUORIVEL</div>
    <div class="contact-bar">
      <span><svg width="12" height="16" viewBox="0 0 12 16"><path d="M6 0C2.7 0 0 2.6 0 5.8 0 10 6 16 6 16S12 10 12 5.8C12 2.6 9.3 0 6 0Z" fill="#1e6fb4"/><circle cx="6" cy="6" r="2.2" fill="#fff"/></svg>Company address</span>
      <span><svg width="14" height="14" viewBox="0 0 14 14"><path d="M3 0L5.5 3.5 4 5.5C5 7.5 6.5 9 8.5 10L10.5 8.5 14 11 12.5 13.5C6 14 0 8 .5 1.5Z" fill="#1e6fb4"/></svg>00 321 654 987</span>
      <span><svg width="16" height="12" viewBox="0 0 16 12"><rect x="1" y="1" width="14" height="10" fill="none" stroke="#1e6fb4" stroke-width="1.8"/><path d="M1 1L8 7 15 1" fill="none" stroke="#1e6fb4" stroke-width="1.8"/></svg>www.quorivel.com</span>
    </div>
  </article>
</div>
</body>
</html>
```